Bright And Steady Web Design & Marketing

Will award a 2nd place prize of $100.00 if someone can come up with a logo to match this design!
Updates

Okay, I'm really looking to see some better designs here. What do you think will bring the best designs out? Please remember with all future submissions I'm looking for a cartoon style / illustrator style website. I'm not sure what the technical term is for it, so I uploaded some images in the brief.

Target Market(s)

Small Business Owners

Industry/Entity Type

Marketing

Logo Text

BrightAndSteady.example

Number of Pages Required

1 page

Colors

Designer to choose colors to be used in the design.

Requirements
Must have
• Logo should say BrightAndSteady.example I would like more than just a text logo. I want some sort of cool custom graphic / icon with it that will look nice on shirts/hats/etc

```html
<!DOCTYPE html>
<html lang="en">
<head>
<meta charset="utf-8">
<title>Bright And Steady Web Design &amp; Marketing</title>
<link href="https://fonts.googleapis.com/css2?family=Montserrat:wght@400;600;700;800&family=Open+Sans:wght@400;600&display=swap" rel="stylesheet">
<style>
:root{
  --cyan:#1fb4df;
  --ink:#2b2b2b;
  --text:#6f6f6f;
  --muted:#9a9a9a;
  --light:#f4f4f4;
  --footer:#2f2f2f;
  --white:#ffffff;
  --orange:#f26b3a;
}
*{margin:0;padding:0;box-sizing:border-box}
html,body{width:1200px;height:4762px;overflow:hidden}
body{position:relative;background:var(--white);font-family:"Open Sans",Arial,sans-serif;color:var(--text)}
.abs{position:absolute}

/* hero */
.hero{position:absolute;left:0;top:0;width:1200px;height:673px;
  background:linear-gradient(160deg,#5b5753 0%,#47433f 45%,#3a3836 100%)}
.hero-photo{position:absolute;inset:0;background:radial-gradient(ellipse at 70% 75%,rgba(190,150,110,.35),transparent 55%),radial-gradient(ellipse at 20% 80%,rgba(120,130,140,.3),transparent 50%)}
.topbar{position:absolute;left:0;top:0;width:1200px;height:30px;border-bottom:1px solid rgba(255,255,255,.12)}
.topbar span{position:absolute;top:10px;font-size:9px;color:#d8d8d8;letter-spacing:.3px;white-space:nowrap}
.topbar-btn{position:absolute;right:113px;top:5px;width:100px;height:20px;background:var(--cyan);color:#fff;font:600 8px "Montserrat",sans-serif;text-align:center;line-height:20px;letter-spacing:1px}
.nav{position:absolute;left:0;top:30px;width:1200px;height:50px;border-bottom:1px solid rgba(255,255,255,.12)}
.logo{position:absolute;display:flex;align-items:center;gap:6px;font:700 10px "Montserrat",sans-serif;color:#fff;white-space:nowrap}
.logo i{display:block;width:10px;height:10px;background:var(--cyan)}
.nav-link{position:absolute;top:22px;font:600 10px "Montserrat",sans-serif;color:#e6e6e6;letter-spacing:1.5px;white-space:nowrap}
.nav-link.active{color:var(--cyan)}
.nav-link.active::after{content:"";position:absolute;left:0;right:0;bottom:-8px;height:2px;background:var(--cyan)}
.hero-kicker{position:absolute;left:0;width:1200px;top:220px;text-align:center;font:600 17px "Montserrat",sans-serif;color:#eee;letter-spacing:5px}
.hero-title{position:absolute;left:0;width:1200px;top:248px;text-align:center;font:800 58px/64px "Montserrat",sans-serif;color:#d9d9d9;letter-spacing:7px}
.hero-dash{position:absolute;left:573px;top:390px;width:54px;height:6px;background:repeating-linear-gradient(90deg,#fff 0 6px,transparent 6px 9px)}
.btn{position:absolute;top:414px;width:126px;height:36px;font:700 10px/36px "Montserrat",sans-serif;letter-spacing:1.5px;text-align:center;color:#fff}
.btn-solid{left:464px;background:var(--cyan)}
.btn-outline{left:608px;border:2px solid #fff;line-height:32px}

/* about */
.label{position:absolute;left:0;width:1200px;text-align:center;font:600 10px "Montserrat",sans-serif;color:var(--cyan);letter-spacing:5px}
.section-title{position:absolute;left:0;width:1200px;text-align:center;font:600 22px "Montserrat",sans-serif;color:var(--ink);letter-spacing:8px}
.title-rule{position:absolute;left:280px;width:640px;height:1px;background:#ddd}
.about-copy{position:absolute;left:300px;width:600px;text-align:center;font-size:10px;line-height:17px;color:var(--muted)}
.diff-title{position:absolute;left:0;width:1200px;top:952px;text-align:center;font:700 20px "Montserrat",sans-serif;color:var(--ink);letter-spacing:6px}
.diff-dash{position:absolute;left:583px;top:990px;width:34px;height:4px;background:repeating-linear-gradient(90deg,var(--cyan) 0 4px,transparent 4px 7px)}
.feature{position:absolute;left:0;width:1200px;height:207px}
.feature .shade{position:absolute;top:12px;width:92px;height:183px;background:var(--light)}
.feature .photo{position:absolute;top:0;width:314px;height:207px}
.feature h3{position:absolute;font:700 11px "Montserrat",sans-serif;color:var(--cyan);letter-spacing:2px;text-transform:uppercase;width:330px}
.feature p{position:absolute;font-size:9.5px;line-height:15px;color:var(--muted);width:300px}
.feature.text-left h3,.feature.text-left p{text-align:right}
.feature.text-left h3{left:210px}
.feature.text-left p{left:240px}
.feature.text-right h3,.feature.text-right p{left:610px}

/* services */
.services{position:absolute;left:0;top:2175px;width:1200px;height:676px;background:linear-gradient(180deg,#444 0%,#3a3a3a 100%)}
.services .backdrop{position:absolute;inset:0;background:radial-gradient(ellipse at 85% 40%,rgba(120,110,100,.35),transparent 50%),radial-gradient(ellipse at 15% 60%,rgba(110,110,110,.25),transparent 50%)}
.service{position:absolute;width:210px;text-align:center}
.service svg{display:block;margin:0 auto}
.service span{display:block;margin-top:12px;font:600 10px/16px "Montserrat",sans-serif;color:#f0f0f0;letter-spacing:2.5px;text-transform:uppercase}

/* team */
.team-card{position:absolute;top:2965px;width:232px;height:324px;overflow:hidden}
.team-card .portrait{position:absolute;inset:0}
.team-card .band{position:absolute;left:0;bottom:0;width:100%;height:70px;background:var(--cyan)}
.team-card .band::before{content:"";position:absolute;left:-20px;top:-14px;width:272px;height:28px;border-radius:50%;background:var(--cyan)}
.team-card .name{position:absolute;left:0;width:100%;text-align:center;font:700 11px "Montserrat",sans-serif;color:#fff;letter-spacing:2px}
.team-card .role{position:absolute;left:0;width:100%;text-align:center;font-size:8px;color:#e8f8fd;letter-spacing:1px;text-transform:uppercase}
.team-card.active{background:var(--cyan)}
.team-card.active p{position:absolute;left:24px;width:184px;text-align:center;font-size:8.5px;line-height:14px;color:#eaf9fe}
.circle-btn{position:absolute;left:99px;top:250px;width:34px;height:34px;border-radius:50%;background:var(--orange);color:#fff;font:700 12px/34px "Montserrat",sans-serif;text-align:center}

/* video */
.video{position:absolute;left:0;top:3867px;width:1200px;height:492px;background:linear-gradient(180deg,#5a5652,#403d3a)}
.play{position:absolute;left:549px;top:4030px;width:104px;height:104px;border-radius:50%;background:var(--cyan);border:6px solid rgba(255,255,255,.85)}
.video-title{position:absolute;left:0;width:1200px;top:4170px;text-align:center;font:600 24px "Montserrat",sans-serif;color:#fff;letter-spacing:9px}

/* footer */
.footer{position:absolute;left:0;top:4359px;width:1200px;height:403px;background:var(--footer)}
.footer-heading{position:absolute;font:700 11px "Montserrat",sans-serif;color:#fff;letter-spacing:3px}
.footer-copy{position:absolute;width:220px;font-size:9.5px;line-height:16px;color:#a5a5a5}
.news-thumb{position:absolute;width:38px;height:38px;background:#e6e6e6}
.news-text{position:absolute;width:170px;font-size:9px;line-height:13px;color:#d8d8d8}
.input-line{position:absolute;left:880px;top:4603px;width:210px;height:1px;background:#777}
.footer-rule{position:absolute;left:0;top:4690px;width:1200px;height:1px;background:#444}
.social{position:absolute;top:4717px;width:22px;height:22px;border-radius:50%;border:1px solid #777}
.copyright{position:absolute;left:235px;top:4722px;font-size:9px;color:#888}
</style>
</head>
<body>

<header class="hero">
  <div class="hero-photo" role="img" aria-label="Photo of a designer's desk with sketches and colour swatches, darkened"></div>
  <div class="topbar">
    <span style="left:233px">info@brightandsteady.example</span>
    <span style="left:410px">Phone: (555) 010-2040</span>
    <div class="topbar-btn">CONTACT US NOW</div>
  </div>
  <nav class="nav">
    <div class="logo" style="left:232px;top:20px"><i></i>BrightAndSteady.example</div>
    <div class="nav-link active" style="left:415px">HOME</div>
    <div class="nav-link" style="left:476px">SERVICES &amp; PRICING</div>
    <div class="nav-link" style="left:650px">OUR TEAM</div>
    <div class="nav-link" style="left:752px">CLIENTS/PORTFOLIO</div>
    <div class="nav-link" style="left:905px">CONTACT US</div>
  </nav>
  <div class="hero-kicker">THE DESIGN &amp; MARKETING TEAM THAT ALWAYS PUTS</div>
  <h1 class="hero-title">TRUST &amp; LOYALTY<br>BEFORE PROFITS</h1>
  <div class="hero-dash"></div>
  <div class="btn btn-solid">CONTACT US</div>
  <div class="btn btn-outline">PORTFOLIO</div>
</header>

<section class="about">
  <div class="label" style="top:732px">ABOUT US</div>
  <h2 class="section-title" style="top:752px">THE DESIGN &amp; MARKETING TEAM</h2>
  <div class="title-rule" style="top:790px"></div>
  <p class="about-copy" style="top:805px">We believe that honesty and integrity come before any quick profit. We are a friendly design and marketing company that treats every client like a long term partner, listening closely and building work that grows your business.</p>
  <p class="about-copy" style="top:850px">We are not driven by sales targets but by your success. We take the time to explain our choices, offer fair prices and stay with you long after launch day, so you always know who is looking after your brand.</p>

  <h2 class="diff-title">WHAT MAKES ME DIFFERENT?</h2>
  <div class="diff-dash"></div>

  <div class="feature text-left" style="top:1022px">
    <div class="shade" style="left:565px"></div>
    <div class="photo" style="left:654px;background:linear-gradient(135deg,#8a5a44,#c99a78)" role="img" aria-label="Photo of a woman reading a tablet"></div>
    <h3 style="top:72px">100% Risk Free Engagement</h3>
    <p style="top:96px">If you are unhappy with anything that we deliver, we will make it right at no extra cost to you.</p>
  </div>

  <div class="feature text-right" style="top:1248px">
    <div class="photo" style="left:232px;background:linear-gradient(135deg,#b9bcbf,#e4e5e6)" role="img" aria-label="Photo of a businessman working at a laptop"></div>
    <div class="shade" style="left:546px"></div>
    <h3 style="top:72px">Customer Loyalty Program</h3>
    <p style="top:96px">After 12 months with us you earn rewards, free updates and exclusive loyalty discounts.</p>
  </div>

  <div class="feature text-left" style="top:1470px">
    <div class="shade" style="left:565px"></div>
    <div class="photo" style="left:654px;background:linear-gradient(135deg,#6f8290,#c2ccd2)" role="img" aria-label="Photo of a support team wearing headsets"></div>
    <h3 style="top:82px">24/7 U.S. Based Customer Support</h3>
    <p style="top:106px">Phone &amp; Email</p>
  </div>

  <div class="feature text-right" style="top:1695px">
    <div class="photo" style="left:232px;background:linear-gradient(135deg,#5c5550,#a89a90)" role="img" aria-label="Photo of three colleagues looking at a laptop"></div>
    <div class="shade" style="left:546px"></div>
    <h3 style="top:72px">Unmatched Personal Service</h3>
    <p style="top:96px">As soon as you come to us your project has its own manager, ready to help with your website, content and design work so you always know who to call.</p>
  </div>

  <div class="feature text-left" style="top:1921px">
    <div class="shade" style="left:565px"></div>
    <div class="photo" style="left:654px;background:linear-gradient(135deg,#c7ccd0,#eef0f1)" role="img" aria-label="Photo of a smiling woman at her desk"></div>
    <h3 style="top:82px">Multiple Payment Options Available</h3>
    <p style="top:106px">Monthly Billing, Pay As You Go, Flat Fee Plans</p>
  </div>
</section>

<section class="services">
  <div class="backdrop" role="img" aria-label="Darkened photo of a team working at computers"></div>
</section>
<div class="label" style="top:2230px">OUR SERVICES</div>
<h2 class="section-title" style="top:2252px;color:#fff">WHAT SERVICES DO WE OFFER?</h2>

<div class="service" style="left:250px;top:2340px">
  <svg width="60" height="56" viewBox="0 0 60 56" fill="none" stroke="#fff" stroke-width="2"><rect x="6" y="6" width="48" height="34"/><line x1="6" y1="14" x2="54" y2="14"/><rect x="12" y="19" width="16" height="14"/><line x1="32" y1="21" x2="48" y2="21"/><line x1="32" y1="27" x2="48" y2="27"/><line x1="22" y1="50" x2="38" y2="50"/><line x1="30" y1="40" x2="30" y2="50"/></svg>
  <span>Website Design &amp;<br>Management</span>
</div>
<div class="service" style="left:495px;top:2340px">
  <svg width="60" height="56" viewBox="0 0 60 56" fill="none" stroke="#fff" stroke-width="2"><rect x="8" y="10" width="44" height="34"/><rect x="14" y="24" width="6" height="14"/><rect x="24" y="18" width="6" height="20"/><rect x="34" y="28" width="6" height="10"/><line x1="4" y1="48" x2="56" y2="48"/><line x1="30" y1="4" x2="30" y2="10"/></svg>
  <span>Logo Design &amp;<br>Branding Materials</span>
</div>
<div class="service" style="left:740px;top:2340px">
  <svg width="60" height="56" viewBox="0 0 60 56" fill="none" stroke="#fff" stroke-width="2"><rect x="6" y="10" width="48" height="32"/><line x1="6" y1="18" x2="54" y2="18"/><rect x="12" y="24" width="10" height="8"/><rect x="26" y="24" width="10" height="8"/><rect x="40" y="24" width="8" height="8"/></svg>
  <span>Online Store Design &amp;<br>Management</span>
</div>
<div class="service" style="left:250px;top:2505px">
  <svg width="60" height="56" viewBox="0 0 60 56" fill="none" stroke="#fff" stroke-width="2"><rect x="10" y="12" width="40" height="36"/><path d="M10 12l6-8h28l6 8"/><rect x="18" y="20" width="8" height="8"/><rect x="34" y="20" width="8" height="8"/><rect x="25" y="34" width="10" height="14"/></svg>
  <span>Local SEO<br>Management</span>
</div>
<div class="service" style="left:495px;top:2505px">
  <svg width="60" height="56" viewBox="0 0 60 56" fill="none" stroke="#fff" stroke-width="2"><circle cx="30" cy="22" r="14"/><line x1="30" y1="36" x2="30" y2="50"/><line x1="6" y1="14" x2="54" y2="14"/><line x1="24" y1="22" x2="36" y2="22"/></svg>
  <span>Search Engine<br>Optimization</span>
</div>
<div class="service" style="left:740px;top:2505px">
  <svg width="60" height="56" viewBox="0 0 60 56" fill="none" stroke="#fff" stroke-width="2"><path d="M12 28h8v20h-8z"/><path d="M20 30l10-14 4 2-2 10h14l-2 18H20"/><rect x="36" y="4" width="18" height="12" rx="2"/></svg>
  <span>Social Media<br>Marketing</span>
</div>
<div class="service" style="left:250px;top:2670px">
  <svg width="60" height="56" viewBox="0 0 60 56" fill="none" stroke="#fff" stroke-width="2"><rect x="10" y="4" width="32" height="44"/><line x1="16" y1="14" x2="36" y2="14"/><line x1="16" y1="22" x2="36" y2="22"/><line x1="16" y1="30" x2="30" y2="30"/><path d="M48 10v34l-3 6-3-6V10z"/></svg>
  <span>Marketing Material<br>&amp; Print Design</span>
</div>
<div class="service" style="left:495px;top:2670px">
  <svg width="60" height="56" viewBox="0 0 60 56" fill="none" stroke="#fff" stroke-width="2"><rect x="6" y="16" width="48" height="30" rx="3"/><rect x="20" y="10" width="20" height="6"/><circle cx="30" cy="31" r="9"/><circle cx="30" cy="31" r="4"/></svg>
  <span>Outsourcing<br>Management</span>
</div>
<div class="service" style="left:740px;top:2670px">
  <svg width="60" height="56" viewBox="0 0 60 56" fill="none" stroke="#fff" stroke-width="2"><rect x="14" y="26" width="32" height="22"/><path d="M22 26v-8a8 8 0 0116 0v8"/><line x1="30" y1="34" x2="30" y2="40"/></svg>
  <span>Consulting</span>
</div>

<h2 class="section-title" style="top:2888px;font-weight:700;font-size:21px">MEET OUR TEAM</h2>

<div class="team-card" style="left:111px">
  <div class="portrait" style="background:linear-gradient(160deg,#d9d6d2,#f0eeec)" role="img" aria-label="Portrait of a smiling team member"></div>
  <div class="band"></div>
  <div class="name" style="top:268px">JOHN DOE</div>
  <div class="role" style="top:286px">Web Designer</div>
</div>
<div class="team-card active" style="left:359px">
  <div class="name" style="top:90px">JOHN DOE</div>
  <div class="role" style="top:108px">Project Manager</div>
  <p style="top:138px">Keeps every project on time and on budget, and makes sure each client always has a friendly voice to talk to.</p>
  <div class="circle-btn">+</div>
</div>
<div class="team-card" style="left:610px">
  <div class="portrait" style="background:linear-gradient(160deg,#c9a58a,#ece2d8)" role="img" aria-label="Portrait of a team member on the phone"></div>
  <div class="band"></div>
  <div class="name" style="top:268px">JANE DOE</div>
  <div class="role" style="top:286px">Account Manager</div>
</div>
<div class="team-card" style="left:857px">
  <div class="portrait" style="background:linear-gradient(160deg,#d8b89c,#f3ece6)" role="img" aria-label="Portrait of a smiling team member"></div>
  <div class="band"></div>
  <div class="name" style="top:268px">JANE DOE</div>
  <div class="role" style="top:286px">Marketing Lead</div>
</div>

<div class="abs" style="left:0;top:3327px;width:597px;height:540px;background:linear-gradient(135deg,#d6d3cf,#9d9892)" role="img" aria-label="Photo of two colleagues working at a laptop in a bright office"></div>
<div class="abs" style="left:597px;top:3327px;width:306px;height:270px;background:linear-gradient(135deg,#c7c9cb,#8e9296)" role="img" aria-label="Photo of an open plan office"></div>
<div class="abs" style="left:903px;top:3327px;width:297px;height:270px;background:linear-gradient(135deg,#b4b7ba,#6f7478)" role="img" aria-label="Photo of a team meeting"></div>
<div class="abs" style="left:597px;top:3597px;width:306px;height:270px;background:linear-gradient(135deg,#50606f,#2f3a45)" role="img" aria-label="Group photo of the team"></div>
<div class="abs" style="left:903px;top:3597px;width:297px;height:270px;background:linear-gradient(135deg,#c9cacc,#8a8c8f)" role="img" aria-label="Photo of colleagues talking in the office"></div>

<section class="video" role="img" aria-label="Darkened photo of colleagues looking at a tablet together"></section>
<div class="play"><svg width="92" height="92" viewBox="0 0 92 92"><path d="M38 30v32l26-16z" fill="#fff"/></svg></div>
<h2 class="video-title">HOW WE WORK</h2>

<footer class="footer"></footer>
<div class="logo" style="left:235px;top:4420px"><i></i>BrightAndSteady.example</div>
<p class="footer-copy" style="left:235px;top:4452px">A friendly design and marketing team helping small business owners grow with honest advice and fair pricing.</p>
<p class="footer-copy" style="left:235px;top:4512px">From logos to websites and local search, we stay with you every step of the way.</p>

<h4 class="footer-heading" style="left:600px;top:4420px">LATEST NEWS</h4>
<div class="news-thumb" style="left:606px;top:4450px"></div>
<div class="news-text" style="left:654px;top:4453px">Seven simple ways to improve your website this month</div>
<div class="news-thumb" style="left:606px;top:4510px"></div>
<div class="news-text" style="left:654px;top:4513px">Why local search matters more than ever for shops</div>
<div class="news-thumb" style="left:606px;top:4570px"></div>
<div class="news-text" style="left:654px;top:4573px">How a clear brand builds trust with new customers</div>

<h4 class="footer-heading" style="left:880px;top:4420px">SUBSCRIBE</h4>
<p class="footer-copy" style="left:880px;top:4452px;width:210px">Join our monthly newsletter for friendly tips, news and special offers for small business owners.</p>
<p class="abs" style="left:880px;top:4586px;font-size:9px;color:#8a8a8a">Enter your email address</p>
<div class="input-line"></div>

<div class="footer-rule"></div>
<div class="copyright">© 2024 All rights reserved</div>
<div class="social" style="left:870px"></div>
<div class="social" style="left:900px"></div>
<div class="social" style="left:930px"></div>

</body>
</html>
```